Cafeteria management company.. needs fun, healthy, school lunch menu design!

We need a menu design for cafeteria management company.
We manage several cafeterias and need to convey "healthy", "fun", and entice parents and kids to buy from our daily lunch menu.
We are a local company and have great goodwill/name for service.

go to www.bramleymeals.com to see what our company offers...

This menu will be posted online thru all our schools so we want it to look professional as well.
Currently we use it to communicate lots of pertinent information parents and patrons.
We would like to see designs that include all the attached information, and allows content to be editable going forward..(we change meals throughout the year).

Parents of school aged kids. Kids ages 5-18,
Employees of business..

School

• Looking for a usable template with most areas editable...used for high school and elementary menus
Needs to be easily read and use a font that photocopies well and is popular/accessible by all computers..
There is alot of information to include.
Needs to be 1 page 8.5 x 11.
Can be portrait or landscape
Needs to use the trayhopper jpeg.
Like the use of color, but will always be printed in black and white or photocopied as such.

```html
<!DOCTYPE html>
<html lang="en">
<head>
<meta charset="utf-8">
<title>Healthy Choice Menu: Elementary School</title>
<link rel="stylesheet" href="https://fonts.googleapis.com/css2?family=Arimo:ital,wght@0,400;0,700;1,700&family=Roboto:wght@300;400;700&display=swap">
<style>
:root{
  --ink:#1c1c1c;
  --ink-soft:#4a4a4a;
  --rule:#2a2a2a;
  --grey:#8d8d8d;
  --wash:#d6d6d6;
  --paper:#ffffff;
}
*{box-sizing:border-box;margin:0;padding:0}
html,body{width:1200px;height:927px;overflow:hidden;background:var(--paper)}
body{font-family:Arimo,Arial,sans-serif;color:var(--ink)}
.sheet{position:absolute;left:0;top:0;width:1100px;height:850px;transform:scale(1.0909);transform-origin:0 0}
.abs{position:absolute}
.menu-title{left:108px;top:92px;font-family:Roboto,Arial,sans-serif;font-weight:300;font-size:33px;letter-spacing:-.3px;color:var(--ink)}
.menu-grid{left:108px;top:137px;width:607px;display:grid;grid-template-columns:120px 122px 128px 120px 117px;
  grid-template-rows:58px 20px 75px 15px 75px 18px 72px 17px 68px 15px 20px 75px;border-left:1.5px solid var(--rule);border-right:1.5px solid var(--rule)}
.cell{border-left:1.5px solid var(--rule);text-align:center;font-size:9.6px;line-height:1.22;padding:4px 3px 0;position:relative}
.cell.first{border-left:none}
.day{text-align:left;padding:6px 0 0 12px;border-bottom:1.5px solid var(--rule)}
.day b{display:block;font-family:Roboto,Arial,sans-serif;font-weight:400;font-size:16.5px;letter-spacing:.3px}
.day i{display:block;font-style:italic;font-weight:700;font-size:8.6px;margin-top:1px}
.day span{display:block;font-size:7.6px;margin-top:3px}
.band-label{grid-column:1/6;font-weight:700;font-style:italic;font-size:14px;padding:2px 0 0 3px;color:var(--ink-soft)}
.dates{font-size:8.4px;padding:2px 2px 0;text-align:left;border-top:1px dashed var(--grey);border-bottom:1px dashed var(--grey)}
.opt-wrap{grid-column:1/6;display:grid;grid-template-columns:120px 122px 128px 120px 117px;border:1.5px solid var(--rule);border-left:none;border-right:none;margin-top:2px}
.opt-wrap .cell{padding-top:10px}
.week{left:57px;width:70px;height:18px;line-height:18px;white-space:nowrap;transform:rotate(-90deg);transform-origin:center;font-size:15px;color:var(--ink-soft);text-align:center}
.mark{position:absolute;right:6px;bottom:3px;width:12px;height:12px}
.legend{left:108px;top:682px;font-size:7px;display:flex;gap:18px;align-items:center}
.legend span{display:flex;align-items:center;gap:3px}
.fine-title{left:75px;top:699px;font-weight:700;font-style:italic;font-size:10.5px}
.fine{left:75px;top:713px;width:650px;font-size:7.9px;line-height:1.28}
.brand-mark{left:818px;top:68px;width:32px;height:32px;border-radius:50%;background:var(--ink-soft)}
.brand-name{left:740px;top:163px;width:180px;text-align:center;font-weight:700;font-size:14px;color:var(--ink-soft)}
.brand-tag{left:740px;top:183px;width:180px;text-align:center;font-size:7.5px;color:var(--grey)}
.brand-year{left:740px;top:199px;width:180px;text-align:center;font-size:12px;color:var(--ink-soft)}
.kids-strip{left:762px;top:228px;width:138px;height:24px;background:linear-gradient(90deg,#e0e0e0,#cfcfcf,#e0e0e0);border-radius:6px}
.promo-head{left:745px;top:258px;font-weight:700;font-size:19.5px;letter-spacing:-.3px}
.promo-sub{left:770px;top:282px;font-weight:700;font-size:12px}
.partners{left:805px;top:309px;display:flex;gap:7px}
.partners i{display:block;width:22px;height:12px;border-radius:4px;background:var(--ink-soft)}
.checks{left:744px;top:333px;width:212px;font-size:8.6px;line-height:1.3}
.checks li{list-style:none;display:flex;gap:6px;margin-bottom:9px}
.checks svg{flex:none;margin-top:1px}
.win{left:740px;top:431px;font-weight:700;font-style:italic;font-size:14.5px}
.signup{left:800px;top:450px;font-weight:700;font-size:13px}
.contact{left:742px;top:469px;width:215px;text-align:center;font-size:9.2px;line-height:1.42}
.follow{left:768px;top:521px;font-size:7.6px;font-style:italic;font-weight:700;line-height:1.25}
.follow-btn{left:871px;top:520px;width:55px;height:22px;border-radius:4px;background:var(--wash)}
.plan-head{left:740px;top:557px;font-weight:700;font-style:italic;font-size:12.5px}
.plan-url{left:740px;top:574px;font-size:9px;color:var(--grey)}
.plan-url em{font-style:normal;color:var(--ink-soft)}
.plan-body{left:740px;top:587px;width:222px;font-size:9px;line-height:1.32}
.plan-body b{font-size:9.6px}
.note{font-size:12.6px;line-height:16.6px;color:var(--ink);white-space:nowrap}
.note-red{left:18px;top:135px}
.note-logo{left:928px;top:138px}
.note-icons{left:970px;top:291px}
.note-blue{left:957px;top:568px}
.note-scan{left:63px;top:785px;font-weight:700;font-size:13.2px;line-height:17px;white-space:nowrap}
.callouts{left:0;top:0;width:1100px;height:850px;pointer-events:none}
</style>
</head>
<body>
<div class="sheet">

  <h1 class="abs menu-title">Healthy Choice Menu: Elementary School</h1>

  <div class="abs week" style="top:237px">Week 1</div>
  <div class="abs week" style="top:327px">Week 2</div>
  <div class="abs week" style="top:424px">Week 3</div>
  <div class="abs week" style="top:512px">Week 4</div>

  <div class="abs menu-grid">
    <div class="cell first day"><b>MONDAY</b><i>From the Kettle</i><span>Chicken Veggie Noodle</span></div>
    <div class="cell day"><b>TUESDAY</b><i>From the Kettle</i><span>Tomato Vegetable</span></div>
    <div class="cell day"><b>WEDNESDAY</b><i>From the Kettle</i><span>Chicken Rice</span></div>
    <div class="cell day"><b>THURSDAY</b><i>From the Kettle</i><span>Corn Chowder</span></div>
    <div class="cell day"><b>FRIDAY</b><i>From the Kettle</i><span>Beef Vegetable</span></div>

    <div class="band-label">Healthy Choice</div>

    <div class="cell first">Pineapple Chicken,<br>Veggie Brown Rice,<br>Stir-Fried Veggies,<br>Milk, Sm Oatmeal<br>Cookie
      <svg class="mark" viewBox="0 0 12 12"><rect x=".5" y=".5" width="11" height="11" fill="none" stroke="#222"/><path d="M2 6l3 3 6-8" fill="none" stroke="#222" stroke-width="1.5"/></svg></div>
    <div class="cell">Whole Wheat<br>Spaghetti, Lean Meat<br>or Tomato Sauce,<br>Garlic Roll, Milk,<br>Orange Wedges
      <svg class="mark" viewBox="0 0 12 12"><circle cx="6" cy="6" r="5.2" fill="none" stroke="#222"/></svg></div>
    <div class="cell">2 Pancakes,<br>1/2 Sliced Ham,<br>Cucumber Slices,<br>Milk, Chocolate<br>Pudding</div>
    <div class="cell">Mexican Taco Bake,<br>Tossed Garden Salad,<br>Milk, Low-fat Yogurt</div>
    <div class="cell">Creamy Chicken Pasta,<br>Tossed Green Salad,<br>Milk, Fresh Fruit Salad
      <svg class="mark" viewBox="0 0 12 12"><circle cx="6" cy="6" r="5.2" fill="none" stroke="#222"/></svg></div>

    <div class="cell first dates">Sept. 1-4, Oct. 5-9,</div>
    <div class="cell dates">Nov. 2-6, Nov. 30-Dec. 4,</div>
    <div class="cell dates">Jan. 4-7, Feb. 1-5,</div>
    <div class="cell dates">Mar. 1-5, April 26-30,</div>
    <div class="cell dates">May 24-28, June 21-25</div>

    <div class="cell first">Homemade Meatloaf,<br>Carrots, Smashed<br>Potatoes, Gravy,<br>Milk, 1/2 Banana</div>
    <div class="cell">Turkey Pepperoni<br>Panzaroti,<br>Garden Salad,<br>Milk, Low-fat Yogurt
      <svg class="mark" viewBox="0 0 12 12"><rect x=".5" y=".5" width="11" height="11" fill="none" stroke="#222"/><path d="M2 6l3 3 6-8" fill="none" stroke="#222" stroke-width="1.5"/></svg></div>
    <div class="cell">Glazed Baked Ham,<br>Smashed Potatoes,<br>Veggies, Milk,<br>Grapes
      <svg class="mark" viewBox="0 0 12 12"><rect x=".5" y=".5" width="11" height="11" fill="none" stroke="#222"/><path d="M2 6l3 3 6-8" fill="none" stroke="#222" stroke-width="1.5"/></svg></div>
    <div class="cell">Zesty Italian or Veggie<br>Lasagna, Caesar Salad,<br>Milk, Blueberry Oatmeal<br>Muffin
      <svg class="mark" viewBox="0 0 12 12"><rect x=".5" y=".5" width="11" height="11" fill="none" stroke="#222"/><path d="M2 6l3 3 6-8" fill="none" stroke="#222" stroke-width="1.5"/></svg></div>
    <div class="cell">Roasted Chicken,<br>Smashed Potatoes<br>&amp; Veggies<br>Milk, Orange Wedges</div>

    <div class="cell first dates">Sept. 1-4, Oct. 12-16,</div>
    <div class="cell dates">Nov 9-13, Dec. 7-11,</div>
    <div class="cell dates">Jan. 11-14, Feb. 8-12,</div>
    <div class="cell dates">Mar. 8-12, April 5-9,</div>
    <div class="cell dates">May 3-7, May 31- June 4</div>

    <div class="cell first">Whole Wheat<br>Spaghetti,Lean Meat<br>or Tomato Sauce,<br>Roll, Milk, Apple Crisp
      <svg class="mark" viewBox="0 0 12 12"><rect x=".5" y=".5" width="11" height="11" fill="none" stroke="#222"/><path d="M2 6l3 3 6-8" fill="none" stroke="#222" stroke-width="1.5"/></svg></div>
    <div class="cell">2 Pancakes,<br>1/2 Sliced Ham,<br>Cucumber Slices, Milk,<br>Chocolate Pudding</div>
    <div class="cell">Homemade Goulash,<br>Fresh Garden Salad,<br>Milk, Low-fat Yogurt</div>
    <div class="cell">Mexican Chicken<br>Enchiladas &amp; Rice,<br>Milk, Banana Oatmeal<br>Muffin</div>
    <div class="cell">Roasted Chicken,<br>Smashed Potatoes &amp;<br>Veggies, Milk,<br>Orange Wedges
      <svg class="mark" viewBox="0 0 12 12"><rect x=".5" y=".5" width="11" height="11" fill="none" stroke="#222"/><path d="M2 6l3 3 6-8" fill="none" stroke="#222" stroke-width="1.5"/></svg></div>

    <div class="cell first dates">Sept. 1-4, Oct. 19-23,</div>
    <div class="cell dates">Nov. 16-20, Dec. 14-18,</div>
    <div class="cell dates">Jan. 18-22, Feb. 15-19,</div>
    <div class="cell dates">Mar. 15-19, April 12-16,</div>
    <div class="cell dates">May 10-14, June 7-11</div>

    <div class="cell first">Homemade Chicken<br>Pot Pie, Milk, Grapes</div>
    <div class="cell">Zesty Italian or Veggie<br>Lasagna, Caesar<br>Salad, Milk, Blueberry<br>Oatmeal Muffin
      <svg class="mark" viewBox="0 0 12 12"><circle cx="6" cy="6" r="5.2" fill="none" stroke="#222"/></svg></div>
    <div class="cell">Grilled Chicken Stir-Fry,<br>Steamed Rice, Milk,<br>Apple Sauce</div>
    <div class="cell">Traditional Shepherd's<br>Pie, Garden Salad,<br>Milk, Fresh Fruit Salad
      <svg class="mark" viewBox="0 0 12 12"><circle cx="6" cy="6" r="5.2" fill="none" stroke="#222"/></svg></div>
    <div class="cell">Creamy Chicken Pasta,<br>Tossed Garden Salad,<br>Milk, Fresh Fruit Salad</div>

    <div class="cell first dates">Sept.1-4, Oct. 26-30,</div>
    <div class="cell dates">Nov. 23-27 Dec. 21-25,</div>
    <div class="cell dates">Jan. 25-29, Feb. 22-26,</div>
    <div class="cell dates">Mar. 22-26, April 19-23,</div>
    <div class="cell dates">May 17-21, June 14-18</div>

    <div class="band-label">Optional Meal</div>

    <div class="opt-wrap">
      <div class="cell first">Chopped Chicken<br>Burger, Roasted<br>Potatoes &amp; Veggies,<br>Milk &amp; Dessert</div>
      <div class="cell">Cheesy Pizza,<br>Veggies &amp; Dip,<br>Milk &amp; Dessert</div>
      <div class="cell">Soft Beef Taco,<br>Mexican Rice,<br>Milk &amp; Dessert</div>
      <div class="cell">Pepperoni Pizza,<br>Caesar Salad,<br>Milk &amp; Dessert</div>
      <div class="cell">Oven-Baked Chicken<br>Nuggets,<br>Potato Wedges,<br>Milk &amp; Dessert</div>
    </div>
  </div>

  <div class="abs legend">
    <span><svg width="10" height="10" viewBox="0 0 12 12"><circle cx="6" cy="6" r="5" fill="none" stroke="#222"/></svg>A la carte any smiley-face!</span>
    <span><svg width="10" height="10" viewBox="0 0 12 12"><rect x=".5" y=".5" width="11" height="11" fill="none" stroke="#222"/><path d="M2 6l3 3 6-8" fill="none" stroke="#222" stroke-width="1.5"/></svg>Ingredients used are sourced within<br>100 miles of Atlantic Canada</span>
    <span><svg width="10" height="10" viewBox="0 0 12 12"><path d="M6 .5l1.6 3.6 3.9.4-2.9 2.6.8 3.9L6 9 2.6 11l.8-3.9L.5 4.5l3.9-.4z" fill="#222"/></svg>Vegetarian meals are always available,<br>please ask the cafeteria manager</span>
    <span><svg width="10" height="10" viewBox="0 0 12 12"><circle cx="6" cy="6" r="5" fill="none" stroke="#222"/><path d="M2.5 9.5l7-7" stroke="#222"/></svg>Gluten- Free meal already</span>
    <span><svg width="10" height="10" viewBox="0 0 12 12"><path d="M2 10L10 2M6 10L10 6" stroke="#222"/></svg>Gluten- Free meal by request</span>
  </div>

  <div class="abs fine-title">Healthy Choice Menu:</div>
  <p class="abs fine">Variations may occur due to difference in suppliers, ingredient substitutions, recipe revisions, meal assembly at the cafeteria, and/or seasons of the year. Certain menu items may not be available at all locations. We encourage anyone with food allergies, sensitivities or special dietary needs to contact/notify the cafeteria manager. We will work with you the very best we can. Bramley Meal Service Management Inc. and its employees do not assume responsibility for a particular allergy or sensitivity to any foods we provided in an of our cafeterias.</p>

  <div class="abs brand-mark"></div>
  <div class="abs brand-name">Bramley Meals</div>
  <div class="abs brand-tag">Healthy Food Service Solutions</div>
  <div class="abs brand-year">2011/2012</div>
  <div class="abs kids-strip" role="img" aria-label="Row of cheerful cartoon kid characters"></div>

  <div class="abs promo-head">Be a Tray Hopper!</div>
  <div class="abs promo-sub">go to bramleymeals.com</div>
  <div class="abs partners"><i></i><i></i><i></i><i></i></div>

  <ul class="abs checks">
    <li><svg width="9" height="9" viewBox="0 0 10 10"><path d="M1 5l3 3 5-7" fill="none" stroke="#222" stroke-width="1.4"/></svg><span>Join our e mail list &amp; get GREAT COUPONS on our healthy meals and snacks!</span></li>
    <li><svg width="9" height="9" viewBox="0 0 10 10"><path d="M1 5l3 3 5-7" fill="none" stroke="#222" stroke-width="1.4"/></svg><span>Buy your meal plans online &amp; manage your lunch money!</span></li>
    <li><svg width="9" height="9" viewBox="0 0 10 10"><path d="M1 5l3 3 5-7" fill="none" stroke="#222" stroke-width="1.4"/></svg><span>All names entered into wicked contests. Great prizes available. 100 % opt-in.</span></li>
  </ul>

  <div class="abs win">Win Free Lunch for a Month!</div>
  <div class="abs signup">Sign-up Today!</div>
  <p class="abs contact">If you have a great coupon idea or comment, please let us know! E mail us at:<br>Trayhopper@bramleymeals.com</p>
  <p class="abs follow">Follow us and be fed well<br>@trayhopper on</p>
  <div class="abs follow-btn"></div>

  <div class="abs plan-head">Healthy Meal Plan: Buy Online at</div>
  <div class="abs plan-url">www.bramleymeals.com <em>or by cheque</em></div>
  <p class="abs plan-body">The meal plan may be purchased weekly or monthly. Please make cheque payable to: Bramley Meal Service. See the Cafeteria Manager for details on meal plan purchase. Unused tickets/meals are valid until the end of the current school year. Non-consecutive days are allowed.<br><br><b>Purchase 5 or more meals and receive a 20 % discount per meal</b>, when the plan is purchased weekly/monthy. Menu dates as per meal served, are subject to change. Please contact cafeteria manger for meal/date confirmation.</p>

  <p class="abs note note-red">The<br>shade of<br>red I<br>believe is<br>okay. It<br>still lets<br>all the<br>text be<br>legable<br>on the<br>printed<br>version.</p>
  <p class="abs note note-logo">This unclarity is from<br>using an image version of<br>the logo verses an origi-<br>nal file that would keep<br>it’s sharpness. ( do you<br>have an original file?)</p>
  <p class="abs note note-icons">Similar situation<br>with these logos<br>I used the original<br>image you sent me<br>so they are<br>unclear vs<br>sharp</p>
  <p class="abs note note-blue">The original blue<br>color was lost I<br>updated to a darker<br>shade so that it will<br>be viewable when<br>printe blk&amp;wht</p>
  <p class="abs note-scan">* This is a scan from a print. It has gone through many stages and each takes away some of the detail. The printed copy is sharper than the scaned<br>image. You don’t have any of the pixelation you see in this image.</p>

  <svg class="abs callouts" viewBox="0 0 1100 850">
    <g fill="none" stroke="#222" stroke-width="1">
      <path d="M50 143H118"/>
      <path d="M885 148H925"/>
      <path d="M968 316H915"/>
      <path d="M962 330L930 535"/>
      <path d="M955 577H900"/>
    </g>
  </svg>

</div>
</body>
</html>
```